Real Estate Company Needs a Contemporary/Modern Business Card Design

We need a Contemporary/Modern Business Card Design for a New Real Estate Company based in San Francisco, CA called Colvane Terrish Realtors. We would like to see designs that use the color red for the "Colvane Terrish" and gold for the "Realtors." The design should communicate being Modern and yet Established and Stable.

Industry/Entity Type

Business

```html
<!DOCTYPE html>
<html lang="en">
<head>
<meta charset="utf-8">
<title>Colvane Terrish Realtors – Business Card</title>
<link rel="stylesheet" href="https://fonts.googleapis.com/css2?family=Montserrat:wght@600;700&family=Open+Sans:wght@700&display=swap">
<style>
  :root {
    --brand-red: #d90000;
    --brand-gold: #7b6a2c;
    --paper: #ffffff;
    --canvas: #fdfdfd;
    --card-edge: #bdbdbd;
  }
  * { margin: 0; padding: 0; box-sizing: border-box; }
  html, body {
    width: 1200px;
    height: 849px;
    overflow: hidden;
    background: var(--canvas);
  }
  .sheet {
    position: relative;
    width: 1200px;
    height: 849px;
  }
  .card {
    position: absolute;
    width: 453px;
    height: 240px;
  }
  .card--front {
    left: 120px;
    top: 148px;
    height: 239px;
    background: var(--brand-red);
  }
  .card--back {
    top: 428px;
    background: var(--paper);
    border: 1px solid var(--card-edge);
  }
  .card--back-left { left: 120px; }
  .card--back-right { left: 616px; }

  .brand-mark {
    position: absolute;
    display: block;
  }
  .card--front .brand-mark {
    left: 208px;
    top: 66px;
    width: 37px;
    height: 37px;
  }
  .card--back .brand-mark {
    left: 189px;
    top: 72px;
    width: 74px;
    height: 74px;
  }

  .brand-name {
    position: absolute;
    left: 0;
    right: 0;
    top: 113px;
    text-align: center;
    font-family: "Montserrat", sans-serif;
    font-weight: 700;
    font-size: 15px;
    letter-spacing: 0.24em;
    color: var(--paper);
    text-transform: uppercase;
  }
  .brand-rule {
    position: absolute;
    left: 209px;
    top: 139px;
    width: 35px;
    height: 1px;
    background: var(--brand-gold);
  }
  .brand-tagline {
    position: absolute;
    left: 0;
    right: 0;
    top: 145px;
    text-align: center;
    font-family: "Montserrat", sans-serif;
    font-weight: 700;
    font-size: 12px;
    letter-spacing: 0.08em;
    color: var(--brand-gold);
    text-transform: uppercase;
  }

  .contact {
    position: absolute;
    top: 151px;
  }
  .card--back-left .contact { left: 22px; text-align: left; }
  .card--back-right .contact { left: 0; right: 0; text-align: center; }
  .contact__name {
    font-family: "Montserrat", sans-serif;
    font-weight: 700;
    font-size: 12.5px;
    letter-spacing: 0.06em;
    color: var(--brand-gold);
    text-transform: uppercase;
    margin-bottom: 6px;
  }
  .contact__line {
    font-family: "Open Sans", sans-serif;
    font-weight: 700;
    font-size: 11px;
    line-height: 15px;
    color: var(--brand-red);
  }
</style>
</head>
<body>
<main class="sheet">
  <section class="card card--front" aria-label="Card front">
    <svg class="brand-mark" viewBox="0 0 37 37" aria-hidden="true">
      <circle cx="18.5" cy="18.5" r="16.5" fill="none" stroke="#ffffff" stroke-width="2.5"/>
    </svg>
    <h1 class="brand-name">Colvane Terrish</h1>
    <span class="brand-rule"></span>
    <p class="brand-tagline">Realtors</p>
  </section>

  <section class="card card--back card--back-left" aria-label="Card back, left aligned">
    <svg class="brand-mark" viewBox="0 0 74 74" aria-hidden="true">
      <circle cx="37" cy="37" r="33.5" fill="none" stroke="#d90000" stroke-width="5"/>
    </svg>
    <div class="contact">
      <p class="contact__name">Dana Whitlow</p>
      <p class="contact__line">5550 1842</p>
      <p class="contact__line">dwhitlow@mail.co</p>
      <p class="contact__line">Address goes here</p>
    </div>
  </section>

  <section class="card card--back card--back-right" aria-label="Card back, centred">
    <svg class="brand-mark" viewBox="0 0 74 74" aria-hidden="true">
      <circle cx="37" cy="37" r="33.5" fill="none" stroke="#d90000" stroke-width="5"/>
    </svg>
    <div class="contact">
      <p class="contact__name">Dana Whitlow</p>
      <p class="contact__line">5550 1842</p>
      <p class="contact__line">dwhitlow@mail.co</p>
      <p class="contact__line">Address goes here</p>
    </div>
  </section>
</main>
</body>
</html>
```